Banner for construction site to identify developer

we need a 4 foot by 8 foot banner to hang on the fence of a residential townhome development in Phoenix, Arizona that identifies Tolvane Holdings as the company behind the development/project. Also needs to include the logo, phone number, and web address. Would like to stick with the blue colors provided in the attached logo. The blues should stay the same but the letters in the logo can change to another color if necessary. Feel free to use "Tolvane Holdings" in place of "Tolvane Holdings Group". Looking for use of colors/design to take up space so banner is not just text with a logo.

Target Market(s)

drive by traffic looking at the site

Industry/Entity Type

Real Estate

Colors
0054AA
0677BA
7BADD7
CADEEF
E8F1F8

Requirements
Must have
• company name, phone number and web address

```html
<!DOCTYPE html>
<html lang="en">
<head>
<meta charset="UTF-8">
<title>Tolvane Holdings Group – Site Banner</title>
<link rel="stylesheet" href="https://fonts.googleapis.com/css2?family=Montserrat:wght@400;700;800&display=swap">
<style>
  :root {
    --sky: #1ca8db;
    --charcoal: #404042;
    --white: #ffffff;
    --wave-deep: #0677ba;
    --wave-mid: #7badd7;
    --wave-pale: #cadeef;
  }
  html, body {
    margin: 0;
    padding: 0;
    overflow: hidden;
    background: var(--white);
  }
  .banner {
    position: relative;
    width: 1200px;
    height: 600px;
    overflow: hidden;
    background: var(--white);
    font-family: "Montserrat", sans-serif;
  }
  .wave-texture {
    position: absolute;
    inset: 0;
    width: 1200px;
    height: 440px;
  }
  .brand-name {
    position: absolute;
    left: 100px;
    top: 190px;
    width: 1000px;
    margin: 0;
    color: var(--charcoal);
    font-weight: 700;
    font-size: 94px;
    line-height: 1;
    letter-spacing: -2px;
    text-align: right;
  }
  .brand-name .brand-line {
    display: block;
  }
  .brand-name .brand-line + .brand-line {
    font-size: 80px;
    margin-top: 14px;
    letter-spacing: -1px;
  }
  .contact-band {
    position: absolute;
    left: 0;
    top: 440px;
    width: 1200px;
    height: 160px;
    background: var(--sky);
    color: var(--white);
    text-align: center;
  }
  .contact-phone {
    margin: 18px 0 0;
    font-weight: 800;
    font-size: 76px;
    line-height: 1;
    letter-spacing: 1px;
  }
  .contact-web {
    margin: 14px 0 0;
    font-weight: 400;
    font-size: 40px;
    line-height: 1;
    letter-spacing: 5px;
  }
</style>
</head>
<body>
<main class="banner">
  <svg class="wave-texture" viewBox="0 0 1200 440" role="img" aria-label="Flowing fine-line blue wave pattern" preserveAspectRatio="none">
    <defs>
      <linearGradient id="wave-top" x1="0" y1="0" x2="1" y2="1">
        <stop offset="0" stop-color="var(--wave-pale)" stop-opacity="0.15"/>
        <stop offset="0.5" stop-color="var(--wave-mid)" stop-opacity="0.45"/>
        <stop offset="1" stop-color="var(--wave-deep)" stop-opacity="0.25"/>
      </linearGradient>
      <linearGradient id="wave-bottom" x1="0" y1="0" x2="1" y2="1">
        <stop offset="0" stop-color="var(--wave-deep)" stop-opacity="0.3"/>
        <stop offset="1" stop-color="var(--wave-pale)" stop-opacity="0.1"/>
      </linearGradient>
    </defs>
    <path d="M480 0 C620 60 760 40 860 110 C930 160 960 210 1000 215 C1080 220 1140 240 1200 310 L1200 0 Z" fill="url(#wave-top)"/>
    <path d="M720 0 C820 20 900 80 1000 60 C1080 45 1140 30 1200 40 L1200 0 Z" fill="var(--wave-mid)" fill-opacity="0.25"/>
    <path d="M0 280 C60 270 110 272 150 300 C200 340 230 390 255 440 L0 440 Z" fill="url(#wave-bottom)"/>
  </svg>

  <h1 class="brand-name">
    <span class="brand-line">Tolvane Holdings</span>
    <span class="brand-line">Group</span>
  </h1>

  <section class="contact-band">
    <p class="contact-phone">CALL: (480) 555-0147</p>
    <p class="contact-web">Visit: www.tolvaneholdingsgroup.com</p>
  </section>
</main>
</body>
</html>
```